Civic Counsel and Advocacy Network needs poster design for landlord/tenant cases

We're seeking a poster design (11x17) to spread awareness for services by "Civic Counsel and Advocacy Network". The services they're trying to communicate are regarding housing/landlord/tenant matters.

We'd like the poster to (1) reflect the color scheme and branding of their website www.ccanplumridge.org, (2) contain the following copy: "Everyone needs safe and suitable housing, whether they own a home or rent one. When homelessness threatens, we at CCN help clients free of charge through eviction diversion programs and mortgage/tax foreclosure prevention.", and (3) contain their contact information:

Civic Counsel and Advocacy Network, Inc.
"We are YOUR Law Firm for Housing matters"
Contact us at: (555) 314-6082
housing @ccanplumridge.org
www.ccanplumridge.org

Target Market(s)

People who may be facing eviction or homelessness

Industry/Entity Type

Legal

Colors
0054AA
0677BA
7BADD7
CADEEF
E8F1F8
FFC000
F8CF3A
FAE287
FDF2CF
FEFAEE
EB3D1F
EC4F4E
F09395
F8D3D4
FCEDEE

Requirements
Must have
• Must include colors from website: https://ccanplumridge.org/

```html
<!DOCTYPE html>
<html lang="en">
<head>
<meta charset="utf-8">
<title>Eviction – Civic Counsel and Advocacy Network</title>
<link rel="stylesheet" href="https://fonts.googleapis.com/css2?family=Arimo:wght@400;700&family=Libre+Baskerville&family=Playfair+Display:wght@900&family=Roboto+Condensed&display=swap">
<style>
  :root {
    --brick: #cf614b;
    --cream: #f5e7de;
    --sun: #f0c22e;
    --sun-deep: #e2ae1d;
    --paper: #ececea;
    --navy: #2e4381;
    --gold: #c9a24e;
    --ink: #111111;
    --white: #ffffff;
  }
  * { box-sizing: border-box; margin: 0; padding: 0; }
  html, body { width: 1200px; height: 1200px; overflow: hidden; background: var(--white); }
  .poster {
    position: absolute; left: 232px; top: 40px;
    width: 736px; height: 1120px; overflow: hidden;
    background: var(--navy);
  }
  .poster__bands { position: absolute; inset: 0; }
  .quote {
    position: absolute; left: 40px; top: 712px; width: 656px;
    font: 400 15px/23px "Arimo", Arial, sans-serif; color: var(--ink);
    text-align: center;
  }
  .quote b { font-weight: 700; }
  .quote__mark { font: 700 26px/0 "Arimo", Arial, sans-serif; vertical-align: -6px; }
  .org {
    position: absolute; left: 48px; top: 891px;
    display: flex; align-items: center; gap: 18px;
  }
  .org__circle {
    width: 94px; height: 94px; border-radius: 50%;
    border: 4px solid var(--white); flex: none;
  }
  .org__name {
    font: 400 16px/21px "Libre Baskerville", Georgia, serif;
    color: var(--white); letter-spacing: 0.06em; text-transform: uppercase;
  }
  .tagline {
    position: absolute; left: 538px; top: 876px; width: 151px; height: 116px;
    border-left: 1.5px solid var(--gold); border-bottom: 1.5px solid var(--gold);
    padding: 12px 0 0 11px;
    font: 400 16px/22px "Arimo", Arial, sans-serif; color: var(--gold);
  }
  .tagline::before {
    content: ""; position: absolute; left: 0; top: 0; width: 68px;
    border-top: 1.5px solid var(--gold);
  }
  .tagline b { font-weight: 700; }
  .contact-line {
    position: absolute; left: 46px; top: 1027px; width: 450px; height: 44px;
    border-top: 1.5px solid var(--gold); border-bottom: 1.5px solid var(--gold);
    display: flex; align-items: center; justify-content: center; gap: 10px;
    font: 700 21px/1 "Arimo", Arial, sans-serif; color: var(--gold); letter-spacing: 0.03em;
  }
  .contact-line svg { width: 22px; height: 22px; }
  .links { position: absolute; left: 540px; top: 1024px; list-style: none; }
  .links li {
    display: flex; align-items: center; gap: 8px; height: 28px;
    font: 400 12.5px/1 "Roboto Condensed", Arial, sans-serif; color: var(--white);
    letter-spacing: 0.02em;
  }
  .links svg { width: 17px; height: 17px; }
</style>
</head>
<body>
<main class="poster">
  <svg class="poster__bands" viewBox="0 0 736 1120" width="736" height="1120">
    <rect x="0" y="0" width="736" height="860" fill="var(--brick)"/>
    <g role="img" aria-label="Photo collage: a giant hand tipping a house over while a man, chairs and a red sofa tumble out onto a textured yellow wall">
      <path d="M0 292 C60 282 110 300 170 292 C240 284 290 300 360 296 C430 292 470 276 540 290 C600 300 640 282 690 296 L736 290 L736 700 L0 700 Z" fill="var(--sun)"/>
      <ellipse cx="300" cy="360" rx="150" ry="90" fill="#e6c49a" opacity="0.55"/>
      <ellipse cx="470" cy="500" rx="140" ry="150" fill="#efe3c6" opacity="0.6"/>
      <ellipse cx="590" cy="640" rx="80" ry="45" fill="var(--sun-deep)" opacity="0.7"/>
    </g>
    <path d="M0 640 L40 636 L85 646 L130 634 L180 642 L230 630 L280 640 L330 634 L380 648 L430 636 L480 644 L530 632 L580 642 L630 634 L690 646 L736 636 L736 880 L0 880 Z" fill="var(--paper)"/>
    <path d="M0 812 L50 818 L100 830 L150 822 L200 836 L250 830 L300 842 L350 852 L400 846 L450 836 L500 826 L550 832 L600 822 L650 816 L700 812 L736 808 L736 1120 L0 1120 Z" fill="var(--navy)"/>
    <rect x="48" y="48" width="642" height="201" fill="none" stroke="var(--cream)" stroke-width="2"/>
    <text x="369" y="229" text-anchor="middle" textLength="600" lengthAdjust="spacingAndGlyphs"
      font-family="'Playfair Display', Georgia, serif" font-weight="900" font-size="228" fill="var(--cream)">EVICTION</text>
  </svg>

  <p class="quote"><span class="quote__mark">&ldquo;</span> Everyone needs safe and affordable housing, whether they own a home or rent one.<br>When homelessness threatens, we at <b>CCN</b> help clients <b>free of charge</b> through eviction<br>diversion programs and mortgage/tax foreclosure prevention. <span class="quote__mark">&rdquo;</span></p>

  <div class="org">
    <span class="org__circle"></span>
    <p class="org__name">Civic Counsel and Advocacy<br>Network, Inc.</p>
  </div>

  <p class="tagline">We are<br><b>YOUR Law Firm</b><br>for Housing<br>Matters</p>

  <p class="contact-line">CONTACT US AT
    <svg viewBox="0 0 24 24" fill="none" stroke="currentColor" stroke-width="1.6"><circle cx="12" cy="12" r="10.5"/><path d="M8.5 6.5l2 2.5-1.2 1.4c.8 1.8 2 3 3.8 3.8l1.4-1.2 2.5 2-1.2 1.6c-3.8-.4-7.4-4-7.8-7.8z"/></svg>
    (555) 314-6082</p>

  <ul class="links">
    <li><svg viewBox="0 0 24 24" fill="none" stroke="currentColor" stroke-width="1.4"><rect x="2" y="5" width="20" height="14"/><path d="M2 5l10 8 10-8M2 19l7-7M22 19l-7-7"/></svg>housing@ccanplumridge.org</li>
    <li><svg viewBox="0 0 24 24" fill="none" stroke="currentColor" stroke-width="1.4"><circle cx="12" cy="12" r="10"/><ellipse cx="12" cy="12" rx="4.5" ry="10"/><path d="M2 12h20M4 7h16M4 17h16"/></svg>www.ccanplumridge.org</li>
  </ul>
</main>
</body>
</html>
```